Lantern Ridge Tile Inc. Business Card

Looking for business card with embossed raised logo print. Logo provided and want it to be most prominent image on card. Color pallet of black, red, white or charcoal gray preferred for brand recognition. Simple contact information on front and list description of services provided on back. Services included....Custom Showers, Tub Surrounds, Backsplashes, Fireplaces, Floors and more. Dustless Demolition, Lifetime Warranty, Proud member of the Federated Stoneworks Trade Guild

Target Market(s)

High end residential remodel work and new home builders

Contact Information for Business Card

Phone # (402) 555-0193 email address, Lanternridgets@mailvane.net Colby Hanswirth Owner

Requirements
Must have
• Business logo as most prominent image on the front of business card. Along with contact information and name Colby Hanswirth. Would like to see services provided on the back of the card.

```html
<!DOCTYPE html>
<html lang="en">
<head>
<meta charset="utf-8">
<title>Lantern Ridge Tile Inc. Business Card</title>
<link rel="stylesheet" href="https://fonts.googleapis.com/css2?family=Lato:wght@400;700&display=swap">
<style>
  :root {
    --red: #e0242b;
    --black: #0b0b0b;
    --white: #ffffff;
    --ink: #161616;
    --backdrop: #cfcfcf;
  }
  * { box-sizing: border-box; margin: 0; padding: 0; }
  html, body { width: 1200px; height: 900px; overflow: hidden; }
  body {
    background: var(--backdrop);
    font-family: "Lato", Arial, sans-serif;
    position: relative;
  }
  .card {
    position: absolute;
    top: 296px;
    width: 540px;
    height: 308px;
    border-radius: 14px;
    overflow: hidden;
    box-shadow: 0 10px 28px rgba(0,0,0,0.28);
  }
  .card--front { left: 40px; background: var(--white); }
  .card--back { left: 620px; background: var(--black); }

  .brand { display: flex; align-items: center; gap: 10px; }
  .brand__mark { background: var(--red); flex: none; }
  .brand__name { color: var(--red); font-weight: 700; letter-spacing: 0.02em; }

  .card--front .brand { position: absolute; left: 28px; top: 24px; }
  .card--front .brand__mark { width: 22px; height: 22px; }
  .card--front .brand__name { font-size: 22px; }

  .contact { position: absolute; left: 28px; top: 80px; color: var(--ink); }
  .contact__name { color: var(--red); font-weight: 700; font-size: 21px; }
  .contact__role { font-size: 14px; margin-bottom: 12px; }
  .contact__line { display: flex; align-items: center; gap: 8px; font-size: 14px; margin-top: 6px; }
  .contact__line svg { width: 14px; height: 14px; flex: none; }

  .divider {
    position: absolute; left: 290px; top: 92px;
    width: 1.5px; height: 140px; background: var(--red);
  }

  .services { position: absolute; left: 312px; top: 84px; list-style: none; }
  .services li {
    font-size: 16px; color: var(--ink); line-height: 22px;
    display: flex; align-items: center; gap: 8px;
  }
  .services li::before {
    content: ""; width: 9px; height: 9px; border-radius: 50%;
    background: var(--red); flex: none;
  }

  .membership {
    position: absolute; left: 0; bottom: 0; width: 100%; height: 46px;
    background: var(--black); color: var(--red);
    font-size: 16px; display: flex; align-items: center; padding-left: 28px;
  }

  .card--back .brand {
    position: absolute; inset: 0; justify-content: center; gap: 14px;
  }
  .card--back .brand__mark { width: 40px; height: 40px; }
  .card--back .brand__name { font-size: 34px; }
</style>
</head>
<body>
  <section class="card card--front">
    <div class="brand">
      <span class="brand__mark"></span>
      <span class="brand__name">Lantern Ridge Tile Inc.</span>
    </div>

    <div class="contact">
      <p class="contact__name">Colby Hanswirth</p>
      <p class="contact__role">Owner</p>
      <p class="contact__line">
        <svg viewBox="0 0 16 16" aria-hidden="true"><path fill="#e0242b" d="M3 1.5h3l1.2 3.2-1.8 1.3a9 9 0 0 0 4.6 4.6l1.3-1.8 3.2 1.2v3c0 .8-.7 1.5-1.5 1.5C6.6 14.5 1.5 9.4 1.5 3 1.5 2.2 2.2 1.5 3 1.5z"/></svg>
        (402) 555-0193
      </p>
      <p class="contact__line">
        <svg viewBox="0 0 16 16" aria-hidden="true"><rect x="1" y="3" width="14" height="10" rx="1" fill="#e0242b"/><path d="M1.5 3.5 8 9l6.5-5.5" fill="none" stroke="#fff" stroke-width="1.3"/></svg>
        Lanternridgets@mailvane.net
      </p>
    </div>

    <span class="divider"></span>

    <ul class="services">
      <li>Custom Showers</li>
      <li>Tub Surrounds</li>
      <li>Backsplashes</li>
      <li>Fireplaces</li>
      <li>Floors and more</li>
      <li>Dustless Demolition</li>
      <li>Lifetime Warranty</li>
    </ul>

    <p class="membership">Proud member of the Federated Stoneworks Trade Guild</p>
  </section>

  <section class="card card--back">
    <div class="brand">
      <span class="brand__mark"></span>
      <span class="brand__name">Lantern Ridge Tile Inc.</span>
    </div>
  </section>
</body>
</html>
```